Marrowgate Gemworks Website revamp

Hi,

We need a working WordPress theme, not just a .PSD file. Thank you.

We need a complete revamp of our website. We sell lab grown diamonds online. We sell the idea that everyone should be able to afford a diamond. Thus our diamonds are priced very reasonably. Our selling point "the joy of giving and receiving a diamond in a little box".

Our range of products includes rings, bangles, necklace, ear rings etc. We currently only operate in Singapore. Some photos of our products are on our websites.

Need.
- Clean look and feel, simplistic preferably white and soft colours
- Easy to navigate
- No banners
- E Com
- Introduction page
- Willing to change logo if needed

Existing page: www.marrowgategemworks.com

Target Market(s)

Young ladies
Ladies
Men buying for ladies
Young boyfriends fresh out of school buying for love ones
Working ladies to match what they wear to work

Industry/Entity Type

Online

Requirements
Must have
• ECOM. Product shopping cart
Pictures uploads
Intro page
Nice to have
• Pastel colors preferred. - Color scheme is important in our business to create a long term impression. Color scheme will also be used for next potential project, i.e. packaging design.

Should not have
• Should not have old style fonts.

```html
<!DOCTYPE html>
<html lang="en">
<head>
<meta charset="utf-8">
<title>Marrowgate Gemworks</title>
<link href="https://fonts.googleapis.com/css2?family=Alegreya:ital@1&family=Parisienne&display=swap" rel="stylesheet">
<style>
  :root {
    --backdrop: #e6f2e7;
    --panel: #ffffff;
    --ink: #7a6e5a;
    --rule: #8a7e68;
    --butter: #f9d86b;
    --sage: #e2ecd6;
    --silver-light: #f1f1f1;
    --silver-dark: #b9bcbf;
  }
  * { margin: 0; padding: 0; box-sizing: border-box; }
  html, body { width: 1200px; height: 720px; overflow: hidden; }
  body { position: relative; background: var(--backdrop); font-family: "Alegreya", serif; }
  .backdrop-pattern { position: absolute; inset: 0; background: var(--backdrop); }
  .panel {
    position: absolute; left: 128px; top: 56px; width: 961px; height: 610px;
    background: var(--panel);
    clip-path: polygon(22px 0, calc(100% - 22px) 0, 100% 22px, 100% calc(100% - 22px), calc(100% - 22px) 100%, 22px 100%, 0 calc(100% - 22px), 0 22px);
  }
  .brand {
    position: absolute; left: 57px; top: 84px;
    font-family: "Alegreya", serif; font-style: italic; font-size: 26px;
    color: var(--ink); line-height: 1;
  }
  .main-nav { position: absolute; top: 78px; left: 0; width: 100%; }
  .main-nav a {
    position: absolute; font-style: italic; font-size: 19px; color: var(--ink);
    text-decoration: none; white-space: nowrap;
  }
  .nav-rule {
    position: absolute; left: 289px; top: 123px; width: 634px; height: 4px;
    border-top: 1px solid var(--rule); border-bottom: 1px solid var(--rule);
  }
  .hero-photo {
    position: absolute; left: 355px; top: 230px; width: 544px; height: 234px;
    background: linear-gradient(180deg, var(--silver-light) 0%, #dcdedf 55%, var(--silver-dark) 100%);
  }
  .hero-tag {
    position: absolute; left: 75px; font-family: "Parisienne", cursive;
    color: #ffffff; line-height: 1; display: flex; align-items: center;
  }
  .hero-tag.lead { top: 412px; width: 252px; height: 54px; background: var(--butter); font-size: 38px; padding-left: 10px; }
  .hero-tag.title { top: 477px; width: 461px; height: 67px; background: var(--sage); font-size: 54px; letter-spacing: 6px; padding-left: 14px; }
</style>
</head>
<body>
  <div class="backdrop-pattern" role="img" aria-label="Soft mint floral damask pattern"></div>
  <main class="panel">
    <div class="brand">Marrowgate Gemworks</div>
    <nav class="main-nav">
      <a href="#" style="left:389px">Home</a>
      <a href="#" style="left:461px">Shop</a>
      <a href="#" style="left:526px">Our Story</a>
      <a href="#" style="left:625px">Our Diamond</a>
      <a href="#" style="left:749px">Contact Us</a>
    </nav>
    <div class="nav-rule"></div>
    <div class="hero-photo" role="img" aria-label="Row of six silver diamond engagement rings"></div>
    <div class="hero-tag lead">The Beauty of</div>
    <div class="hero-tag title">Diamond Rings</div>
  </main>
</body>
</html>
```